Home Security Company Business Card

Looking for a eye catching business card that is non traditional and stands out but yet still looks professional. It should include all the pertinent information such as name, title, address, telephone, e-mail, website address should definitely stand out and then finally the logo.

Target Market(s)

Residential and Commercial accounts mostly upscale accounts

Industry/Entity Type

Security

Contact Information for Business Card

Name
Title
Address
Office #
Cell #
E-mail
Website

Font styles to use
Serif
Sans Serif

Requirements
Must have
• Logo, two sided color configuration
Nice to have
• You decide
Should not have
• There really aren't any.

```html
<!DOCTYPE html>
<html lang="en">
<head>
<meta charset="utf-8">
<title>Harborline Security Systems – Business Card</title>
<link rel="stylesheet" href="https://fonts.googleapis.com/css2?family=Arimo:wght@400;700&display=swap">
<style>
  :root {
    --backdrop: #3a332f;
    --card: #1c1c1d;
    --card-edge: #262627;
    --brand-red: #9a1a12;
    --title-gold: #d8901c;
    --text-light: #f2f2f2;
    --text-muted: #b9b9b9;
    --divider: #8a8a8a;
    --mark-grey: #5a5a5c;
  }
  * { margin: 0; padding: 0; box-sizing: border-box; }
  html, body { width: 1200px; height: 787px; overflow: hidden; }
  body {
    background: var(--backdrop);
    font-family: "Arimo", Arial, sans-serif;
    position: relative;
  }
  .card {
    position: absolute;
    top: 245px;
    width: 520px;
    height: 297px;
    background: var(--card);
    border: 1px solid var(--card-edge);
    border-radius: 3px;
    box-shadow: 0 10px 24px rgba(0,0,0,0.35);
  }
  .card-back { left: 50px; }
  .card-front { left: 630px; }

  /* brand name with plain mark */
  .brand {
    position: absolute;
    display: flex;
    align-items: center;
    gap: 12px;
    white-space: nowrap;
  }
  .brand-dot { flex: none; border-radius: 50%; }
  .brand-name { font-weight: 400; }

  /* back side */
  .card-back .brand {
    top: 70px; left: 0; right: 0;
    flex-direction: column;
    gap: 18px;
  }
  .card-back .brand-dot { width: 78px; height: 78px; background: var(--mark-grey); }
  .card-back .brand-name { font-size: 18px; letter-spacing: 2px; color: var(--text-muted); }
  .back-website {
    position: absolute;
    top: 222px; left: 0; right: 0;
    text-align: center;
    font-size: 13px;
    letter-spacing: 5px;
    color: var(--text-light);
  }

  /* front side */
  .card-front .brand {
    top: 62px; left: 0; right: 0;
    justify-content: center;
  }
  .card-front .brand-dot { width: 52px; height: 52px; background: var(--title-gold); }
  .card-front .brand-name { font-size: 17px; color: var(--brand-red); }

  .contact-person {
    position: absolute;
    top: 150px; left: 40px; width: 210px;
    text-align: right;
  }
  .person-name { color: var(--brand-red); font-size: 20px; }
  .person-title { color: var(--title-gold); font-size: 15px; margin-top: 3px; }
  .address { color: var(--text-light); font-size: 14px; line-height: 1.45; margin-top: 10px; }

  .divider {
    position: absolute;
    top: 160px; left: 268px;
    width: 1px; height: 100px;
    background: var(--divider);
  }

  .contact-list {
    position: absolute;
    top: 166px; left: 285px;
    list-style: none;
  }
  .contact-list li {
    display: flex; align-items: center; gap: 10px;
    color: var(--text-light);
    font-size: 15px;
    height: 23px;
  }
  .contact-list svg { width: 14px; height: 14px; fill: var(--brand-red); flex: none; }
</style>
</head>
<body>

  <section class="card card-back" aria-label="Business card back">
    <div class="brand">
      <span class="brand-dot" aria-hidden="true"></span>
      <span class="brand-name">Harborline Security Systems Inc</span>
    </div>
    <div class="back-website">www.example.com</div>
  </section>

  <section class="card card-front" aria-label="Business card front">
    <div class="brand">
      <span class="brand-dot" aria-hidden="true"></span>
      <span class="brand-name">Harborline Security Systems Inc</span>
    </div>

    <div class="contact-person">
      <div class="person-name">Daniel Marsh</div>
      <div class="person-title">President</div>
      <div class="address">2170 Linden Avenue<br>Brookvale, NY 11020</div>
    </div>

    <div class="divider"></div>

    <ul class="contact-list">
      <li>
        <svg viewBox="0 0 16 16" aria-hidden="true"><path d="M2 5c0-2 2-3 6-3s6 1 6 3v1h-3V5H5v1H2zM4 7h8l2 6H2z"/></svg>
        555 0142 2253
      </li>
      <li>
        <svg viewBox="0 0 16 16" aria-hidden="true"><path d="M5 1h6a1 1 0 0 1 1 1v12a1 1 0 0 1-1 1H5a1 1 0 0 1-1-1V2a1 1 0 0 1 1-1zm0 2v9h6V3z"/></svg>
        555 0187 5335
      </li>
      <li>
        <svg viewBox="0 0 16 16" aria-hidden="true"><path d="M1 3h14v10H1zm1.5 1.2L8 8.5l5.5-4.3z"/></svg>
        daniel@example.com
      </li>
      <li>
        <svg viewBox="0 0 16 16" aria-hidden="true"><circle cx="8" cy="8" r="7"/><path d="M1 8h14M8 1c3 3 3 11 0 14M8 1c-3 3-3 11 0 14" stroke="#1c1c1d" stroke-width="1.2" fill="none"/></svg>
        www.example.com
      </li>
    </ul>
  </section>

</body>
</html>
```